Business card required for IT Consultancy Business - Tealbrook Consulting.
Company provides the whole nine yards of services across IT Architecture, design and execution.
Basically we provide consulting services to help businesses make sure their technology is enabling their business strategy.
Design for front and back required.
We would like the front of the card to inlcude:
Name
Title
Mobile number
email address
www.tbkc.com.au
Company logos attached.
Thank you
Industry/Entity Type
Business
Contact Information for Business Card
Name
Title
Mobile number
email address
www.tbkc.com.au
Look and feel
Each slider illustrates characteristics of the customer's brand and the style your logo design should communicate.

```html
<!DOCTYPE html>
<html lang="en">
<head>
<meta charset="utf-8">
<title>Tealbrook Consulting – Business Card</title>
<link href="https://fonts.googleapis.com/css2?family=Montserrat:wght@700;800&family=Arimo:wght@400;700&display=swap" rel="stylesheet">
<style>
  :root {
    --orange: #ec4a24;
    --orange-light: #f26c48;
    --blue: #1b6fc8;
    --ink: #1c1c1c;
    --paper: #ffffff;
    --backdrop: #e9e6e2;
  }
  html, body {
    margin: 0;
    width: 1200px;
    height: 900px;
    overflow: hidden;
    background: var(--backdrop);
    font-family: "Arimo", Arial, sans-serif;
  }
  .stage { position: relative; width: 1200px; height: 900px; }
  .card {
    position: absolute;
    width: 680px;
    height: 388px;
    box-shadow: 0 8px 24px rgba(0,0,0,.18);
    overflow: hidden;
  }

  /* Back of card */
  .card--back {
    left: 120px; top: 40px;
    background: linear-gradient(100deg, var(--orange) 0%, var(--orange-light) 100%);
  }
  .back-brand {
    position: absolute; left: 0; right: 0; top: 120px;
    display: flex; align-items: center; justify-content: center; gap: 18px;
  }
  .back-brand__dot {
    width: 54px; height: 54px; border-radius: 50%; background: var(--ink);
  }
  .back-brand__name {
    font-family: "Montserrat", Arial, sans-serif;
    font-weight: 800; font-size: 46px; color: var(--ink); letter-spacing: .5px;
  }
  .back-web {
    position: absolute; left: 0; right: 0; bottom: 30px;
    text-align: center; font-size: 18px; letter-spacing: 1.5px; color: var(--ink);
  }
  .back-web::after {
    content: ""; display: block; width: 250px; height: 5px; margin: 6px auto 0;
    background: #2b2b2b;
  }

  /* Front of card */
  .card--front { left: 400px; top: 472px; background: var(--paper); }
  .front-bar { position: absolute; right: 0; height: 6px; background: var(--orange); }
  .front-bar--top { top: 0; width: 300px; }
  .front-bar--bottom { bottom: 18px; width: 340px; }
  .front-mark {
    position: absolute; left: 92px; top: 98px;
    width: 190px; height: 190px; border-radius: 50%; background: var(--blue);
  }
  .front-info { position: absolute; left: 350px; top: 46px; width: 290px; }
  .front-brand {
    font-family: "Montserrat", Arial, sans-serif;
    font-weight: 800; font-size: 25px; color: var(--blue); line-height: 1.1;
    padding-bottom: 12px; border-bottom: 2px solid var(--orange);
  }
  .person { margin-top: 14px; font-family: "Montserrat", Arial, sans-serif; font-weight: 800; font-size: 20px; letter-spacing: .5px; }
  .person__first { color: var(--orange); }
  .person__last { color: var(--blue); }
  .title { font-size: 20px; color: var(--ink); margin-top: 2px; }
  .phone { font-size: 18px; color: var(--ink); margin-top: 16px; letter-spacing: .5px; }
  .contacts { list-style: none; margin: 12px 0 0; padding: 0; }
  .contacts li { display: flex; align-items: center; gap: 8px; font-size: 18px; color: var(--ink); margin-bottom: 10px; }
  .contacts svg { width: 22px; height: 22px; flex: none; }
</style>
</head>
<body>
<main class="stage">
  <section class="card card--back" aria-label="Card back">
    <div class="back-brand">
      <span class="back-brand__dot"></span>
      <span class="back-brand__name">Tealbrook Consulting</span>
    </div>
    <div class="back-web">www.tbkc.com.au</div>
  </section>

  <section class="card card--front" aria-label="Card front">
    <span class="front-bar front-bar--top"></span>
    <span class="front-bar front-bar--bottom"></span>
    <span class="front-mark"></span>
    <div class="front-info">
      <div class="front-brand">Tealbrook Consulting</div>
      <div class="person"><span class="person__first">MARLOW</span> <span class="person__last">FINCH</span></div>
      <div class="title">CEO</div>
      <div class="phone">014-2875-360</div>
      <ul class="contacts">
        <li>
          <svg viewBox="0 0 22 22" aria-hidden="true"><circle cx="11" cy="11" r="10" fill="#ec4a24"/><circle cx="11" cy="11" r="7" fill="#fff"/><rect x="8" y="6" width="6" height="10" rx="1" fill="#1b6fc8"/></svg>
          <span>014-2875-360</span>
        </li>
        <li>
          <svg viewBox="0 0 22 22" aria-hidden="true"><circle cx="11" cy="11" r="10" fill="#ec4a24"/><circle cx="11" cy="11" r="7" fill="#fff"/><rect x="6" y="8" width="10" height="7" fill="#1b6fc8"/><path d="M6 8l5 4 5-4" stroke="#fff" fill="none"/></svg>
          <span>hello@tbkc.com.au</span>
        </li>
        <li>
          <svg viewBox="0 0 22 22" aria-hidden="true"><circle cx="11" cy="11" r="10" fill="#ec4a24"/><circle cx="11" cy="11" r="7" fill="#fff"/><circle cx="11" cy="11" r="5" fill="#1b6fc8"/></svg>
          <span>www.tbkc.com.au</span>
        </li>
      </ul>
    </div>
  </section>
</main>
</body>
</html>
```